Stationary for Hair Cosmetic company

We mainly sell hair thickening products www.morvello-wellform.de/morvello-hair/ Hair thickening products are a smart and easy solution for thinning hair for both men and women. We sell very information oriented in an honest undramatic manner.

We would like to see a decent color and style that is suitable for men and women. It shall be rather modern with a vintage spin as our own product (Morvello Bottle). Please use our logo (attatched).

Please bias your design to the bottle. To give you an idea: Chalk design like http://de.pixaverum.com/id/48213597 or one-color watercolor like http://de.pixaverum.com/id/63925180 is appreciated but not necessary.

Good but rejected designs will get compensation.

Target Market(s)

Wide range in demographics: age 20-55; 45% male, 55% women; issues with hair loss; self-conscious

Industry/Entity Type

Hair

Colors
3377b5
33a6d7
32b7a4
cbdf83
fbf289
fee18a
f9bb93
f05157

Requirements
Must have
• trustworthiness
Nice to have
• Chalk design like http://de.pixaverum.com/id/48213597 or one-color watercolor like http://de.pixaverum.com/id/63925180 is appreciated but not necessary

```html
<!DOCTYPE html>
<html lang="en">
<head>
<meta charset="utf-8">
<title>Morvello Stationery</title>
<link rel="stylesheet" href="https://fonts.googleapis.com/css2?family=Cinzel:wght@400;700&family=Courier+Prime:ital,wght@0,400;0,700;1,700&display=swap">
<style>
  :root {
    --backdrop: #e6e4e1;
    --ink-dark: #1c1b1b;
    --paper-dark: #232222;
    --paper-light: #f7f7f5;
    --silver: #d2d2d2;
    --silver-soft: #8e8e8e;
    --ink-grey: #5a5a5a;
    --ornament-dark: #3a3939;
    --ornament-light: #dcdcda;
    --lettering-light: #c4c4c2;
  }
  * { box-sizing: border-box; margin: 0; padding: 0; }
  html, body { width: 864px; height: 1200px; overflow: hidden; }
  body { background: var(--backdrop); position: relative; font-family: "Courier Prime", "Courier New", monospace; }

  .piece { position: absolute; box-shadow: 0 6px 18px rgba(0,0,0,.18); overflow: hidden; }
  .frame { position: absolute; inset: 8px; border: 1px solid currentColor; opacity: .35; pointer-events: none; }
  .frame::after { content: ""; position: absolute; inset: 3px; border: 1px solid currentColor; }

  .brand { display: flex; flex-direction: column; align-items: center; gap: 6px; }
  .brand-dot { width: 32px; height: 32px; border-radius: 50%; border: 2px solid currentColor; }
  .brand-name { font-family: "Cinzel", Georgia, serif; font-weight: 700; letter-spacing: .22em; font-size: 15px; }

  .ornament { display: block; margin: 0 auto; }

  .rule-diamond { display: flex; align-items: center; gap: 6px; margin: 6px 8px; }
  .rule-diamond::before, .rule-diamond::after { content: ""; flex: 1; height: 1px; background: currentColor; opacity: .6; }
  .rule-diamond span { width: 6px; height: 6px; background: currentColor; transform: rotate(45deg); opacity: .8; }

  /* business cards */
  .card { top: 50px; width: 360px; height: 214px; padding: 16px 18px; display: flex; gap: 14px; }
  .card .brand { width: 86px; justify-content: center; }
  .card .brand-name { font-size: 13px; letter-spacing: .16em; }
  .card .details { flex: 1; display: flex; flex-direction: column; justify-content: center; text-align: center; }
  .card-front { left: 60px; background: var(--paper-dark); color: var(--silver); }
  .card-light { left: 444px; background: var(--paper-light); color: var(--ink-dark); }
  .person-name { font-family: "Cinzel", Georgia, serif; font-weight: 700; font-size: 18px; letter-spacing: .08em; line-height: 1.12; }
  .person-role { font-weight: 700; font-style: italic; font-size: 12px; margin: 3px 0 6px; }
  .contact-line { font-size: 9.5px; line-height: 1.4; white-space: nowrap; }

  /* letterhead */
  .letterhead { left: 60px; top: 310px; width: 380px; height: 538px; background: var(--paper-light); color: var(--ink-dark); padding: 26px 34px; }
  .letterhead .brand { margin-bottom: 8px; }
  .letterhead .brand-name { font-size: 13px; }
  .letterhead .rule-diamond { margin: 0 60px 20px; }
  .salutation { font-size: 10px; margin-bottom: 12px; }
  .letter-body { font-size: 8.5px; line-height: 1.75; color: var(--ink-grey); margin-bottom: 12px; text-align: justify; }
  .letter-sign { position: absolute; right: 40px; bottom: 56px; text-align: right; font-size: 8px; line-height: 1.5; font-weight: 700; font-style: italic; }

  /* folder */
  .folder { left: 480px; top: 310px; width: 324px; height: 538px; background: var(--paper-dark); color: var(--silver); padding-top: 46px; text-align: center; }
  .folder .brand-name { font-size: 18px; }
  .folder .brand-dot { width: 40px; height: 40px; }
  .folder .rule-diamond { margin: 14px 70px 0; }
  .folder-address { position: absolute; left: 0; right: 0; bottom: 112px; font-weight: 700; font-style: italic; font-size: 19px; letter-spacing: .02em; }
  .folder-flourish-top { position: absolute; left: 0; right: 0; bottom: 146px; }
  .folder-flourish-bottom { position: absolute; left: 0; right: 0; bottom: 84px; }

  /* envelope */
  .envelope { left: 60px; top: 890px; width: 744px; height: 260px; background: var(--paper-light); color: var(--ink-dark); padding: 30px 40px; }
  .envelope .brand { align-items: flex-start; width: 190px; }
  .envelope .brand-name { font-size: 14px; }
  .envelope .rule-diamond { margin: 8px 0 0; width: 150px; }
  .sender { font-size: 9px; line-height: 1.5; margin-top: 8px; color: var(--ink-grey); }
  .envelope-lettering { position: absolute; right: 46px; top: 40px; font-family: "Cinzel", Georgia, serif; font-weight: 700; font-size: 40px; line-height: 1.12; letter-spacing: .02em; color: var(--lettering-light); text-align: left; }
</style>
</head>
<body>

  <section class="piece card card-front" aria-label="Business card, dark front">
    <div class="frame"></div>
    <div class="brand">
      <span class="brand-dot"></span>
      <span class="brand-name">MORVELLO</span>
    </div>
    <div class="details">
      <svg class="ornament" width="110" height="10" role="img" aria-label="Silver flourish ornament"><rect width="110" height="10" rx="5" fill="var(--ornament-dark)"/></svg>
      <div class="rule-diamond"><span></span></div>
      <p class="person-name">ADRIAN<br>KELLER</p>
      <p class="person-role">General Manager</p>
      <p class="contact-line">Phone: +38 (000) 555-01-27</p>
      <p class="contact-line">e-mail: adrian@morvello-wellform.de</p>
      <p class="contact-line">www.morvello-wellform.de</p>
      <div class="rule-diamond"><span></span></div>
      <svg class="ornament" width="110" height="10" role="img" aria-label="Silver flourish ornament"><rect width="110" height="10" rx="5" fill="var(--ornament-dark)"/></svg>
    </div>
  </section>

  <section class="piece card card-light" aria-label="Business card, light version">
    <div class="frame"></div>
    <div class="brand">
      <span class="brand-dot"></span>
      <span class="brand-name">MORVELLO</span>
    </div>
    <div class="details">
      <svg class="ornament" width="110" height="10" role="img" aria-label="Flourish ornament"><rect width="110" height="10" rx="5" fill="var(--ornament-light)"/></svg>
      <div class="rule-diamond"><span></span></div>
      <p class="person-name">ADRIAN<br>KELLER</p>
      <p class="person-role">General Manager</p>
      <p class="contact-line">Phone: +38 (000) 555-01-27</p>
      <p class="contact-line">e-mail: adrian@morvello-wellform.de</p>
      <p class="contact-line">www.morvello-wellform.de</p>
      <div class="rule-diamond"><span></span></div>
      <svg class="ornament" width="110" height="10" role="img" aria-label="Flourish ornament"><rect width="110" height="10" rx="5" fill="var(--ornament-light)"/></svg>
    </div>
  </section>

  <section class="piece letterhead" aria-label="Letterhead">
    <div class="brand">
      <span class="brand-dot"></span>
      <span class="brand-name">MORVELLO</span>
    </div>
    <div class="rule-diamond"><span></span></div>
    <p class="salutation">Dear Mr. Hallberg,</p>
    <p class="letter-body">We are glad to share our new range of hair thickening care with you. Each product is made to support fine hair gently and is easy to use every day, for men and women alike.</p>
    <p class="letter-body">Our team explains every step in plain words, so you always know what you apply and why. Samples of the full range are enclosed with this letter for you to try at home.</p>
    <p class="letter-body">Please find the details of your order below and do not hesitate to contact us with any question. We look forward to hearing from you.</p>
    <div class="letter-sign">
      <p>Phone: +38 (000) 555-01-27</p>
      <p>e-mail: adrian@morvello-wellform.de</p>
      <p>www.morvello-wellform.de</p>
    </div>
  </section>

  <section class="piece folder" aria-label="Presentation folder">
    <div class="frame"></div>
    <div class="brand">
      <span class="brand-dot"></span>
      <span class="brand-name">MORVELLO</span>
    </div>
    <div class="rule-diamond"><span></span></div>
    <svg class="ornament folder-flourish-top" width="120" height="12" role="img" aria-label="Silver flourish above the web address"><rect width="120" height="12" rx="6" fill="var(--ornament-dark)"/></svg>
    <p class="folder-address">morvello-wellform.de</p>
    <svg class="ornament folder-flourish-bottom" width="180" height="12" role="img" aria-label="Silver flourish below the web address"><rect width="180" height="12" rx="6" fill="var(--ornament-dark)"/></svg>
  </section>

  <section class="piece envelope" aria-label="Envelope">
    <div class="frame"></div>
    <div class="brand">
      <span class="brand-dot"></span>
      <span class="brand-name">MORVELLO</span>
      <div class="rule-diamond"><span></span></div>
      <p class="sender">Morvello GmbH<br>Lindenstraße 12<br>20095 Hamburg</p>
    </div>
    <p class="envelope-lettering">MORVELLO-<br>WELLFORM<br>.DE</p>
  </section>

</body>
</html>
```